Web Design Project

We need a website for a new public relations firm offering PR, advertising, media buying, design and social media. Target clients are professional service firms such as lawyers or CPAs. Looks should be clean and look expensive.

Target Market(s)

Professional service firms. Think business to business companies like consultancy firms.

Industry/Entity Type

Professional Service

Colors

Designer to choose colors to be used in the design.

Requirements
Must have
• Site pages for the purpose of design will include Home, Services, Experience, Bios and Contact Us

```html
<!DOCTYPE html>
<html lang="en">
<head>
<meta charset="utf-8">
<title>NORVEL – Marketing · PR · Advertising</title>
<link href="https://fonts.googleapis.com/css2?family=Open+Sans:wght@400;600&display=swap" rel="stylesheet">
<style>
:root{
  --ink:#111111;
  --text:#555555;
  --muted:#8a8a8a;
  --logo:#8c8c8c;
  --rule:#dddddd;
  --band:#2e2e2e;
  --info-bg:#f4f4f4;
  --footer:#333333;
  --footer-text:#cfcfcf;
  --circle-top:#a9a9ad;
  --circle-bottom:#7f7f85;
  --hero-top:#8fb0d3;
  --hero-mid:#d9e3ec;
  --hero-bottom:#a3bbd0;
  --white:#ffffff;
}
*{margin:0;padding:0;box-sizing:border-box}
html,body{width:1058px;height:1200px;overflow:hidden;background:var(--white)}
body{font-family:"Open Sans",Arial,sans-serif;color:var(--text);position:relative}
.page{position:relative;width:1058px;height:1200px}

.site-header{position:absolute;left:0;top:0;width:1058px;height:125px}
.brand{position:absolute;left:92px;top:24px}
.brand-name{font-size:50px;font-weight:400;color:var(--logo);letter-spacing:2px;line-height:56px}
.brand-tagline{font-size:11px;color:var(--ink);letter-spacing:1px;margin-top:8px;padding-left:22px}
.header-phone{position:absolute;right:88px;top:31px;font-size:19px;color:var(--ink);display:flex;align-items:center;gap:5px}
.main-nav{position:absolute;right:88px;top:80px;display:flex;gap:30px;font-size:13px;text-transform:uppercase}
.main-nav a{color:var(--muted);text-decoration:none}
.main-nav a.is-current{color:var(--ink)}

.hero{position:absolute;left:0;top:125px;width:1058px;height:389px;
  background:linear-gradient(180deg,var(--hero-top) 0%,var(--hero-mid) 55%,var(--hero-bottom) 100%)}
.hero-caption{position:absolute;left:0;top:514px;width:1058px;height:67px;background:var(--band);
  display:flex;align-items:center;justify-content:center;color:var(--white);font-size:20px;font-weight:600;text-transform:uppercase}
.slider-arrow{position:absolute;top:18px}
.slider-arrow.prev{left:104px}
.slider-arrow.next{right:104px}

.welcome{position:absolute;left:0;top:622px;width:1058px;text-align:center}
.section-title{font-size:29px;font-weight:600;color:var(--ink);text-transform:uppercase;line-height:40px}
.welcome p{width:800px;margin:1px auto 0;font-size:13.2px;line-height:23px}
.divider{position:absolute;left:88px;top:773px;width:883px;height:1px;background:var(--rule)}

.services{position:absolute;left:0;top:806px;width:1058px;text-align:center}
.service-list{list-style:none;position:absolute;top:50px;left:0;width:1058px}
.service{position:absolute;width:180px;text-align:center}
.service-icon{width:92px;height:92px;border-radius:50%;margin:0 auto;
  background:linear-gradient(180deg,var(--circle-top),var(--circle-bottom));display:flex;align-items:center;justify-content:center}
.service-name{display:block;margin-top:14px;font-size:14px;color:var(--text);text-transform:uppercase;letter-spacing:.3px}

.contact-bar{position:absolute;left:0;top:1025px;width:1058px;height:84px;background:var(--info-bg);font-size:12.5px;color:var(--text)}
.contact-item{position:absolute;display:flex;align-items:center;gap:10px;line-height:20px}

.site-footer{position:absolute;left:0;top:1109px;width:1058px;height:91px;background:var(--footer);color:var(--footer-text);font-size:12px}
.footer-nav{position:absolute;left:89px;top:19px}
.footer-nav a{color:var(--footer-text);text-decoration:none}
.footer-nav .sep{margin:0 10px}
.copyright{position:absolute;left:89px;top:52px}
.social{position:absolute;left:856px;top:35px;display:flex;gap:8px}
.social span{width:22px;height:22px;border-radius:50%;background:#6a6a6a;display:flex;align-items:center;justify-content:center}
</style>
</head>
<body>
<div class="page">

<header class="site-header">
  <div class="brand">
    <div class="brand-name">NORVEL</div>
    <div class="brand-tagline">Marketing · PR · Advertising</div>
  </div>
  <div class="header-phone">
    <svg width="16" height="16" viewBox="0 0 16 16"><circle cx="8" cy="8" r="6.5" fill="none" stroke="#555" stroke-width="1.2"/><path d="M5 8.5l2 2 4-5" fill="none" stroke="#555" stroke-width="1.2"/></svg>
    555 210 4830
  </div>
  <nav class="main-nav">
    <a class="is-current" href="#">Home</a>
    <a href="#">Services</a>
    <a href="#">Experience</a>
    <a href="#">Bios</a>
    <a href="#">Contact Us</a>
  </nav>
</header>

<div class="hero" role="img" aria-label="Hero photograph: businessman on a boardwalk facing a city skyline under a bright sky"></div>
<div class="hero-caption">
  <svg class="slider-arrow prev" width="18" height="32" viewBox="0 0 18 32"><path d="M16 1L2 16l14 15" fill="none" stroke="#ccc" stroke-width="2"/></svg>
  Duis ultrices augue lacinia interdum vestibulum
  <svg class="slider-arrow next" width="18" height="32" viewBox="0 0 18 32"><path d="M2 1l14 15L2 31" fill="none" stroke="#ccc" stroke-width="2"/></svg>
</div>

<section class="welcome">
  <h1 class="section-title">Welcome to NORVEL</h1>
  <p>Maecenas vel tempor erat, non ornare erat. Donec vel neque a neque hendrerit tempor. Donec rutrum turpis quis felis laoreet, sit amet rutrum ex maximus. Vivamus id lorem ipsum. Morbi condimentum leo nisl, lacinia efficitur dolor ultricies nec. Donec blandit ante nunc, sit amet tristique lacus porta eu. Aenean ut laoreet felis, sed euismod ligula.</p>
</section>

<div class="divider"></div>

<section class="services">
  <h2 class="section-title">Our Services</h2>
  <ul class="service-list">
    <li class="service" style="left:87px">
      <div class="service-icon"><svg width="34" height="26" viewBox="0 0 34 26" fill="#fff"><circle cx="12" cy="7" r="5"/><path d="M2 24c0-7 4-10 10-10s10 3 10 10z"/><circle cx="23" cy="8" r="4"/><path d="M24 14c5 0 8 3 8 9h-8z"/></svg></div>
      <span class="service-name">Public Relations</span>
    </li>
    <li class="service" style="left:264px">
      <div class="service-icon"><svg width="32" height="28" viewBox="0 0 32 28" fill="#fff"><rect x="2" y="9" width="6" height="8"/><path d="M8 9l16-7v22L8 17z"/><rect x="26" y="1" width="3" height="24"/><rect x="5" y="17" width="4" height="8"/></svg></div>
      <span class="service-name">Advertising</span>
    </li>
    <li class="service" style="left:441px">
      <div class="service-icon"><svg width="32" height="26" viewBox="0 0 32 26" fill="#fff"><path d="M11 5V2h10v3h-2V4h-6v1z"/><rect x="1" y="6" width="30" height="19" rx="2"/><rect x="1" y="13" width="30" height="2" fill="#8f8f95"/><rect x="14" y="12" width="4" height="4" fill="#fff"/></svg></div>
      <span class="service-name">Media Buying</span>
    </li>
    <li class="service" style="left:618px">
      <div class="service-icon"><svg width="30" height="30" viewBox="0 0 30 30" fill="#fff"><path d="M28 2L13 19l-3-2z"/><path d="M10 18c-4 0-6 3-6 6 0 2-2 3-3 3 4 2 11 1 11-6z"/></svg></div>
      <span class="service-name">Design</span>
    </li>
    <li class="service" style="left:796px">
      <div class="service-icon"><svg width="44" height="34" viewBox="0 0 44 34" fill="none" stroke="#fff" stroke-width="1"><path d="M3 26L18 8 29 4 41 14 27 31 21 20 3 26M18 8l3 12 20-6M29 4l-8 16M18 8l9 23M3 26l24 5"/><g fill="#fff"><circle cx="3" cy="26" r="2"/><circle cx="18" cy="8" r="2"/><circle cx="29" cy="4" r="2"/><circle cx="41" cy="14" r="2"/><circle cx="27" cy="31" r="2"/><circle cx="21" cy="20" r="2"/></g></svg></div>
      <span class="service-name">Social Media</span>
    </li>
  </ul>
</section>

<section class="contact-bar">
  <div class="contact-item" style="left:107px;top:21px">
    <svg width="22" height="26" viewBox="0 0 22 26" fill="none" stroke="#999" stroke-width="1.6"><path d="M2 4h18v21H2z"/><path d="M6 8v13M11 8v13M16 8v13" /></svg>
    <span>55, Building name, streetname<br>City - Zip code</span>
  </div>
  <div class="contact-item" style="left:353px;top:32px">
    <svg width="26" height="26" viewBox="0 0 26 26" fill="#999"><path d="M3 3l6-2 4 6-3 3c2 4 4 6 8 8l3-3 6 4-2 6C14 25 1 12 3 3z"/></svg>
    <span>Phone: 555 210 4831</span>
  </div>
  <div class="contact-item" style="left:576px;top:32px">
    <svg width="26" height="26" viewBox="0 0 26 26" fill="#999"><rect x="1" y="8" width="5" height="17"/><rect x="7" y="6" width="18" height="19"/><rect x="12" y="1" width="10" height="6" fill="none" stroke="#999"/><g fill="#f4f4f4"><rect x="10" y="11" width="3" height="2"/><rect x="15" y="11" width="3" height="2"/><rect x="20" y="11" width="3" height="2"/><rect x="10" y="16" width="3" height="2"/><rect x="15" y="16" width="3" height="2"/><rect x="20" y="16" width="3" height="2"/></g></svg>
    <span>Fax : 555 210 4832</span>
  </div>
  <div class="contact-item" style="left:786px;top:32px">
    <svg width="26" height="18" viewBox="0 0 26 18" fill="#999"><path d="M0 0h26v18H0z"/><path d="M1 1l12 9 12-9" fill="none" stroke="#f4f4f4" stroke-width="1.5"/></svg>
    <span>E-mail : info@norvel-pr.com</span>
  </div>
</section>

<footer class="site-footer">
  <nav class="footer-nav">
    <a href="#">Home</a><span class="sep">|</span><a href="#">Services</a><span class="sep">|</span><a href="#">Experience</a><span class="sep">|</span><a href="#">Bios</a><span class="sep">|</span><a href="#">Contact Us</a>
  </nav>
  <div class="copyright">Copyright &copy; 2014 &nbsp;NORVEL. &nbsp;All rights reserved.</div>
  <div class="social">
    <span></span><span></span><span></span>
    <span><svg width="13" height="9" viewBox="0 0 13 9" fill="none" stroke="#ddd"><rect x=".5" y=".5" width="12" height="8"/><path d="M.5 .5l6 4 6-4"/></svg></span>
  </div>
</footer>

</div>
</body>
</html>
```